Flyer, poster, banner and social media titles designs for Community Renewal Guidlines

The Shared Guidelines for Community Renewal provide a nationally agreed framework to guide recovery policy and practice across Australia. The Principles support recovery practitioners, governments, non-government organisations and communities to deliver effective, community-centred recovery outcomes.
The Principles have recently been refreshed through extensive consultation and we require a contemporary visual identity and design suite that will increase awareness, engagement and practical application of the Principles.
The redesign will cover:
• A4 Brochure (primary publication)
• A3 Poster
• Pull up banner
• Social Media Tiles
The new design should:
• Create a recognisable brand for the Shared Guidelines.
• Appeal to both experienced and emerging recovery practitioners.
• Reflect contemporary disaster recovery practice.
• Feel people-focused rather than government-focused.
• Support future resources such as videos, implementation guides, presentations and workshop materials.
• Remain relevant for several years without requiring a major redesign.
Target Audience
• Disaster recovery practitioners
• Government agencies
• Non-government organisations
• Community recovery workers
• Recovery managers and leaders
• Community stakeholders and volunteers
The visual identity should reflect the six Principles:
• Understanding Context
• Recognising Complexity
• Community-Centred Approaches
• Coordination
• Communication
• Capacity Building
The design should communicate:
• Recovery is centred on people and communities.
• Recovery is collaborative and involves many sectors.
• Recovery is adaptive, inclusive and evidence-informed.
• Recovery supports resilience and long-term wellbeing.
• The Principles provide practical guidance for recovery practice.
We are looking for:
• Modern and professional
• Warm and approachable
• Human-centred
• Inclusive and accessible
• Australian in context
• Visually engaging
• Suitable for print and digital use
We would like to avoid:
• Images of disaster destruction
• Emergency response imagery (fire trucks, flashing lights, etc.)
• Overly corporate or bureaucratic designs
• Designs that focus on deficits rather than recovery and growth
Consider themes such as:
• Connection and collaboration
• Communities and people
• Growth, recovery and renewal
Accessibility
Designs should:
• Meet accessibility best practice
• Use clear typography
• Achieve strong colour contrast
• Be suitable for both digital and print formats

Deliverables
1. Principles Brochure
• A4 trifold size x 2 (online and print friendly version)
• A side to include cover side, logos side and overview of principles.
• B side full details of the principles
• Graphic to highlight the 3 c’s concept (RECOVERY Context, complexity, community centred, coordinate, communicate and capacity). Currently 3 circles.
• Can be printed and distributed electronically
2. Poster
• A1 and A3 versions
• Suitable for office and workshop display
3. Pull-Up Banner - 850 mm (W) × 2000 mm (H)
• Conference and event use
• High visual impact
• Strong branding and concise messaging
4. Social Media Tiles x 3
Updates

We are providing an extension and increasing the budget following feedback from designers. We are wanting the resources to look and feel different from the existing designs, considering either a different colour palette in the designs or different motif with the leave design. Any nature based designs should consider the Australian fauna or flora. Also suggest avoiding images in the designs. The principles are not numbered or liner in the concept of how they function. Happy to answer any further questions and thank you for your suggested concepts.

Target Market(s)

Disaster recovery practitioners, Government agencies , Non-government organisations, Community recovery workers and Community stakeholders and volunteers

Industry/Entity Type

Disaster recovery

Colors

Designer to choose colors to be used in the design.

Requirements
Must have
• Modern, warm, visually engaging, human-centred, Australian in context and different to the current design.
Nice to have
• Symbols for each principles
Should not have
• Images of disaster destruction, Emergency response imagery, Overly corporate or bureaucratic designs, Designs that focus on deficits rather than recovery and growth, avoid too much black

```html
<!DOCTYPE html>
<html lang="en">
<head>
<meta charset="utf-8">
<title>Shared Guidelines for Community Renewal – Design Suite</title>
<link href="https://fonts.googleapis.com/css2?family=Outfit:wght@400;500;600;700&family=Nunito+Sans:wght@400;600;700;800&display=swap" rel="stylesheet">
<style>
:root{
  --navy:#0e3552;--navy-deep:#0a2a42;--cream:#f6f2e8;--ink:#1d2b38;
  --green:#6b9a2c;--purple:#5b3f8c;--orange:#e2672a;--teal:#17838a;--blue:#1f5fa8;--yellow:#e6a817;
  --lime:#9cbf3a;--sky:#4aa7b8;
}
*{box-sizing:border-box;margin:0;padding:0}
html,body{width:1200px;height:800px;overflow:hidden;background:#fff}
body{position:relative;font-family:"Nunito Sans",sans-serif;color:var(--ink)}
.section-label{position:absolute;font-family:"Outfit",sans-serif;font-weight:600;font-size:17px;letter-spacing:.5px;color:#111}
.side-label{position:absolute;left:8px;width:50px;text-align:center;font-family:"Outfit",sans-serif;font-size:13px;color:#111;line-height:1.35}
.side-label small{font-size:10px;display:block}
.sheet{position:absolute;box-shadow:0 1px 4px rgba(0,0,0,.25);overflow:hidden;background:var(--cream)}
.eyebrow{font-family:"Outfit",sans-serif;font-weight:500;color:#fff;letter-spacing:.3px}
.title{font-family:"Outfit",sans-serif;font-weight:500;line-height:.95;color:#fff}
.title .accent{color:var(--lime);display:block}
.tagline{color:#fff;font-weight:600;line-height:1.55}
.tagline em{font-style:normal;color:var(--yellow)}
.flora{position:absolute;border-radius:50% 50% 40% 60%}
.wave{position:absolute;left:0;bottom:0;width:100%}
/* brochure A */
.brochure-a{left:68px;top:42px;width:473px;height:273px;display:flex}
.panel{position:relative;height:100%}
.panel-cover{width:166px;background:var(--navy);padding:44px 14px 0}
.panel-cover .eyebrow{font-size:8px}
.panel-cover .title{font-size:25px;margin-top:5px}
.panel-cover .tagline{font-size:8.5px;margin-top:16px}
.panel-intro{width:145px;padding:28px 14px 0 20px}
.panel-heading{font-family:"Outfit",sans-serif;font-weight:600;font-size:9.5px;color:var(--navy);line-height:1.3;letter-spacing:.2px}
.panel-text{font-size:7px;line-height:1.5;margin-top:10px;color:#333}
.panel-list{width:162px;padding:18px 14px 0 26px;background:#faf7f0}
.mini-list{list-style:none;margin-top:14px}
.mini-list li{display:flex;align-items:center;gap:8px;font-size:6.8px;height:21.5px}
.dot-icon{width:18px;height:18px;border-radius:50%;display:flex;align-items:center;justify-content:center;flex:none}
.dot-icon svg{width:62%;height:62%}
/* brochure B */
.brochure-b{left:68px;top:329px;width:473px;height:257px;display:flex}
.col{flex:1;padding:14px 4px 0;border-right:1px solid #e3ddcf;text-align:center}
.col:last-child{border:0}
.col .dot-icon{width:40px;height:40px;margin:0 auto}
.col h3{font-family:"Outfit",sans-serif;font-weight:600;font-size:6.2px;line-height:1.3;margin-top:8px;height:18px;letter-spacing:-.1px}
.col ul{text-align:left;padding-left:10px;margin-top:8px}
.col li{font-size:5.3px;line-height:1.5;margin-bottom:7px;color:#333}
/* poster */
.poster{left:564px;top:42px;width:350px;height:544px}
.poster-head{position:absolute;left:0;top:0;width:100%;height:260px}
.poster-copy{position:absolute;left:24px;top:26px}
.poster-copy .eyebrow{font-size:11.5px}
.poster-copy .title{font-size:38px;margin-top:4px}
.poster-copy .tagline{font-size:9px;margin-top:10px}
.ring{position:absolute;left:0;top:162px;width:350px;height:270px}
.values{position:absolute;left:20px;top:432px;width:230px;display:flex}
.value{flex:1;text-align:center;font-size:5.6px;line-height:1.4;padding:0 3px;border-right:1px solid #cfc8b8}
.value:last-child{border:0}
.value svg{width:22px;height:22px;display:block;margin:0 auto 4px}
.poster-foot{position:absolute;left:24px;top:506px;font-size:7px;line-height:1.45;color:#333}
/* banner */
.banner{left:951px;top:43px;width:215px;height:558px;background:var(--cream)}
.banner-rail{position:absolute;left:946px;top:40px;width:225px;height:5px;background:#cfd3d6;border-radius:2px}
.banner-copy{position:absolute;left:20px;top:34px}
.banner-copy .eyebrow{font-size:10.5px}
.banner-copy .title{font-size:31px;margin-top:6px}
.banner-copy .tagline{font-size:9px;margin-top:12px;line-height:1.7}
.banner-list{position:absolute;left:26px;top:234px;list-style:none}
.banner-list li{display:flex;align-items:center;gap:12px;height:36px;font-family:"Outfit",sans-serif;font-weight:600;font-size:9.5px;line-height:1.1}
.banner-list .dot-icon{width:28px;height:28px}
.banner-foot{position:absolute;left:20px;top:500px;color:#fff;font-size:7.5px;line-height:1.6;font-weight:600}
.banner-foot b{font-size:8.5px;display:block;line-height:1.35}
/* tiles */
.tile{top:628px;width:156px;height:150px}
.tile-head{position:absolute;left:10px;top:12px;display:flex;gap:10px}
.tile-head .dot-icon{width:34px;height:34px}
.tile-title{font-family:"Outfit",sans-serif;font-weight:600;font-size:9px;line-height:1.15;margin-top:9px}
.tile-title.long{font-size:8px}
.tile-text{position:absolute;left:54px;top:52px;width:98px;font-size:7px;line-height:1.5;color:#333}
.tile-foot{position:absolute;left:0;bottom:7px;width:100%;text-align:center;color:#fff;font-size:6px;font-weight:700;letter-spacing:.2px}
</style>
</head>
<body>
<svg width="0" height="0" style="position:absolute" aria-hidden="true">
  <defs>
    <symbol id="i-leaf" viewBox="0 0 24 24"><path d="M12 21V11M12 13c-5 0-7-4-7-8 4 0 7 3 7 8zM12 14c0-5 3-8 8-8 0 5-3 8-8 8z" fill="none" stroke="#fff" stroke-width="1.8" stroke-linecap="round"/></symbol>
    <symbol id="i-ring" viewBox="0 0 24 24"><g fill="#fff"><circle cx="12" cy="3" r="1.4"/><circle cx="18.4" cy="5.6" r="1.4"/><circle cx="21" cy="12" r="1.4"/><circle cx="18.4" cy="18.4" r="1.4"/><circle cx="12" cy="21" r="1.4"/><circle cx="5.6" cy="18.4" r="1.4"/><circle cx="3" cy="12" r="1.4"/><circle cx="5.6" cy="5.6" r="1.4"/><circle cx="12" cy="7.5" r="1"/><circle cx="16.5" cy="12" r="1"/><circle cx="12" cy="16.5" r="1"/><circle cx="7.5" cy="12" r="1"/></g></symbol>
    <symbol id="i-group" viewBox="0 0 24 24"><g fill="none" stroke="#fff" stroke-width="1.8"><circle cx="8" cy="8" r="3"/><circle cx="16" cy="8" r="3"/><path d="M3 20v-3a4 4 0 0 1 8 0v3M13 20v-3a4 4 0 0 1 8 0v3"/></g></symbol>
    <symbol id="i-nodes" viewBox="0 0 24 24"><g fill="none" stroke="#fff" stroke-width="1.6"><path d="M12 12L5 5M12 12l7-7M12 12l-7 7M12 12l7 7"/><circle cx="12" cy="12" r="2.4"/><circle cx="5" cy="5" r="2"/><circle cx="19" cy="5" r="2"/><circle cx="5" cy="19" r="2"/><circle cx="19" cy="19" r="2"/></g></symbol>
    <symbol id="i-chat" viewBox="0 0 24 24"><path d="M4 5h16v11H10l-5 4v-4H4z" fill="none" stroke="#fff" stroke-width="2" stroke-linejoin="round"/></symbol>
    <symbol id="i-sun" viewBox="0 0 24 24"><g fill="none" stroke="#fff" stroke-width="1.7"><circle cx="12" cy="12" r="3"/><path d="M12 2v5M12 17v5M2 12h5M17 12h5M5 5l3.5 3.5M15.5 15.5L19 19M5 19l3.5-3.5M15.5 8.5L19 5"/></g></symbol>
  </defs>
</svg>

<h2 class="section-label" style="left:216px;top:16px">A4 BROCHURE (TRIFOLD)</h2>
<h2 class="section-label" style="left:690px;top:16px">A3 POSTER</h2>
<h2 class="section-label" style="left:991px;top:16px">PULL-UP BANNER</h2>
<p class="side-label" style="top:148px">SIDE A<small>(OUTSIDE)</small></p>
<p class="side-label" style="top:413px">SIDE B<small>(INSIDE)</small></p>

<!-- Brochure side A -->
<section class="sheet brochure-a">
  <div class="panel panel-cover">
    <p class="eyebrow">SHARED GUIDELINES FOR</p>
    <h1 class="title">Community<span class="accent">Renewal</span></h1>
    <p class="tagline">Guiding recovery<br>Strengthening communities<br>Building a <em>resilient Australia</em></p>
    <div class="flora" role="img" aria-label="Illustrated banksia flower with leaves" style="left:38px;top:180px;width:100px;height:80px;background:radial-gradient(circle at 55% 45%,#e0b52a 0 28%,#5f8a2e 45%,rgba(14,53,82,0) 72%)"></div>
  </div>
  <div class="panel panel-intro">
    <h2 class="panel-heading">WORKING TOGETHER<br>FOR RECOVERY</h2>
    <p class="panel-text">Recovery is a shared responsibility. Together, we create stronger, more resilient communities.</p>
    <svg class="wave" viewBox="0 0 145 130" height="130" preserveAspectRatio="none" aria-hidden="true">
      <path d="M0 50C30 20 60 30 80 60s45 60 65 70H0z" fill="#7fb4b8"/>
      <path d="M0 65C30 40 60 50 85 85s40 40 60 45H0z" fill="var(--teal)"/>
      <path d="M0 90C35 70 70 90 100 115l20 15H0z" fill="var(--navy)"/>
    </svg>
  </div>
  <div class="panel panel-list">
    <h2 class="panel-heading">THE SIX PRINCIPLES</h2>
    <p class="panel-text" style="margin-top:8px;font-size:6.6px">The Shared Guidelines for Community Renewal provide a nationally agreed framework to guide recovery practice. They support effective, community-centred recovery outcomes across Australia.</p>
    <ul class="mini-list">
      <li><span class="dot-icon" style="background:var(--green)"><svg><use href="#i-leaf"/></svg></span>Understanding Context</li>
      <li><span class="dot-icon" style="background:var(--purple)"><svg><use href="#i-ring"/></svg></span>Recognising Complexity</li>
      <li><span class="dot-icon" style="background:var(--orange)"><svg><use href="#i-group"/></svg></span>Community-Centred Approaches</li>
      <li><span class="dot-icon" style="background:var(--teal)"><svg><use href="#i-nodes"/></svg></span>Coordination</li>
      <li><span class="dot-icon" style="background:var(--blue)"><svg><use href="#i-chat"/></svg></span>Communication</li>
      <li><span class="dot-icon" style="background:var(--yellow)"><svg><use href="#i-sun"/></svg></span>Capacity Building</li>
    </ul>
  </div>
</section>

<!-- Brochure side B -->
<section class="sheet brochure-b">
  <div class="col"><span class="dot-icon" style="background:var(--green)"><svg><use href="#i-leaf"/></svg></span><h3 style="color:var(--green)">UNDERSTANDING<br>CONTEXT</h3>
    <ul><li>Build on the strengths, history and diversity of each community.</li><li>Recognise local risks, needs and aspirations.</li><li>Respect culture, connections and place.</li><li>Support inclusion and equity.</li></ul></div>
  <div class="col"><span class="dot-icon" style="background:var(--purple)"><svg><use href="#i-ring"/></svg></span><h3 style="color:var(--purple)">RECOGNISING<br>COMPLEXITY</h3>
    <ul><li>Disasters are complex and impacts are far-reaching.</li><li>Needs and circumstances change over time.</li><li>Different perspectives and priorities may create tensions.</li><li>Recovery takes time, adaptation and learning.</li></ul></div>
  <div class="col"><span class="dot-icon" style="background:var(--orange)"><svg><use href="#i-group"/></svg></span><h3 style="color:var(--orange)">COMMUNITY-CENTRED<br>APPROACHES</h3>
    <ul><li>Put communities at the centre.</li><li>Empower people to lead their recovery.</li><li>Value local knowledge, strengths and assets.</li><li>Tailor support to local needs and priorities.</li></ul></div>
  <div class="col"><span class="dot-icon" style="background:var(--teal)"><svg><use href="#i-nodes"/></svg></span><h3 style="color:var(--teal)">COORDINATION</h3>
    <ul><li>Plan, coordinate and adapt together.</li><li>Align actions across sectors and agencies.</li><li>Share information and resources.</li><li>Continuously assess needs and impacts.</li></ul></div>
  <div class="col"><span class="dot-icon" style="background:var(--blue)"><svg><use href="#i-chat"/></svg></span><h3 style="color:var(--blue)">COMMUNICATION</h3>
    <ul><li>Communicate clearly, respectfully and consistently.</li><li>Listen and encourage two-way dialogue.</li><li>Share timely and accurate information.</li><li>Use accessible channels and formats.</li></ul></div>
  <div class="col"><span class="dot-icon" style="background:var(--yellow)"><svg><use href="#i-sun"/></svg></span><h3 style="color:var(--yellow)">CAPACITY<br>BUILDING</h3>
    <ul><li>Strengthen skills, knowledge and leadership.</li><li>Support connection and collaboration.</li><li>Invest in long-term resilience.</li><li>Celebrate progress and learn together.</li></ul></div>
  <svg class="wave" viewBox="0 0 473 50" height="38" preserveAspectRatio="none" aria-hidden="true">
    <path d="M0 20C60 5 120 30 200 25s150-20 273-10V50H0z" fill="var(--sky)"/>
    <path d="M0 30C80 20 150 40 240 35s160-15 233-5V50H0z" fill="var(--teal)"/>
    <path d="M0 40C100 30 200 48 300 42s120-10 173-6V50H0z" fill="var(--lime)"/>
  </svg>
</section>

<!-- Poster -->
<section class="sheet poster">
  <svg class="poster-head" viewBox="0 0 350 260" preserveAspectRatio="none" aria-hidden="true">
    <path d="M0 0h350v190C270 170 220 250 120 240S30 210 0 218z" fill="var(--navy)"/>
    <path d="M250 0c20 20 50 30 100 25v15c-50 5-80-10-105-40z" fill="var(--teal)" opacity=".6"/>
  </svg>
  <div class="poster-copy">
    <p class="eyebrow">SHARED GUIDELINES FOR</p>
    <h1 class="title">Community<span class="accent">Renewal</span></h1>
    <p class="tagline">Guiding recovery. Strengthening communities.<br>Building a <em>resilient Australia.</em></p>
  </div>
  <svg class="ring" viewBox="0 0 350 290" font-family="Outfit,sans-serif" font-weight="600" text-anchor="middle">
    <circle cx="174" cy="143" r="98" fill="none" stroke="var(--navy)" stroke-width="1.3" stroke-dasharray="3 4"/>
    <circle cx="174" cy="143" r="44" fill="#fff" stroke="var(--navy)" stroke-width="1.2"/>
    <text x="174" y="131" font-size="10" fill="var(--navy)">PEOPLE</text>
    <text x="174" y="146" font-size="10" fill="var(--navy)">COMMUNITIES</text>
    <text x="174" y="161" font-size="10" fill="var(--navy)">TOGETHER</text>
    <g fill="#fff" font-size="5.8">
      <circle cx="174" cy="45" r="36" fill="var(--green)"/><use href="#i-leaf" x="160" y="22" width="28" height="28"/><text x="174" y="60">UNDERSTANDING</text><text x="174" y="67">CONTEXT</text>
      <circle cx="270" cy="95" r="35" fill="var(--purple)"/><use href="#i-ring" x="256" y="72" width="28" height="28"/><text x="270" y="111">RECOGNISING</text><text x="270" y="118">COMPLEXITY</text>
      <circle cx="264" cy="200" r="35" fill="var(--orange)"/><use href="#i-group" x="250" y="176" width="28" height="28"/><text x="264" y="213">COMMUNITY-</text><text x="264" y="220">CENTRED</text><text x="264" y="227">APPROACHES</text>
      <circle cx="174" cy="243" r="34" fill="var(--teal)"/><use href="#i-nodes" x="160" y="222" width="28" height="28"/><text x="174" y="262">COORDINATION</text>
      <circle cx="80" cy="202" r="35" fill="var(--blue)"/><use href="#i-chat" x="66" y="180" width="28" height="28"/><text x="80" y="220">COMMUNICATION</text>
      <circle cx="78" cy="98" r="34" fill="var(--yellow)"/><use href="#i-sun" x="64" y="74" width="28" height="28"/><text x="78" y="114">CAPACITY</text><text x="78" y="121">BUILDING</text>
    </g>
  </svg>
  <div class="values">
    <p class="value"><svg viewBox="0 0 24 24"><g fill="none" stroke="var(--green)" stroke-width="1.6"><circle cx="8" cy="8" r="3"/><circle cx="16" cy="8" r="3"/><path d="M3 20v-3a4 4 0 0 1 8 0v3M13 20v-3a4 4 0 0 1 8 0v3"/></g></svg>Recovery is centred on <b>people and communities.</b></p>
    <p class="value"><svg viewBox="0 0 24 24"><g fill="none" stroke="var(--blue)" stroke-width="1.5"><path d="M12 12L5 5M12 12l7-7M12 12l-7 7M12 12l7 7"/><circle cx="12" cy="12" r="2.4"/><circle cx="5" cy="5" r="2"/><circle cx="19" cy="5" r="2"/><circle cx="5" cy="19" r="2"/><circle cx="19" cy="19" r="2"/></g></svg>Recovery is <b>collaborative</b> and involves many sectors.</p>
    <p class="value"><svg viewBox="0 0 24 24"><path d="M12 3l2.6 6 6.4.5-4.9 4.2 1.5 6.3L12 16.6 6.4 20l1.5-6.3L3 9.5 9.4 9z" fill="none" stroke="var(--teal)" stroke-width="1.5"/></svg>Recovery is <b>adaptive, inclusive</b> and evidence-informed.</p>
    <p class="value"><svg viewBox="0 0 24 24"><path d="M12 20s-8-5-8-11a4 4 0 0 1 8-1 4 4 0 0 1 8 1c0 6-8 11-8 11z" fill="none" stroke="var(--green)" stroke-width="1.6"/></svg>Recovery supports <b>resilience</b> and long-term wellbeing.</p>
  </div>
  <p class="poster-foot">The Shared Guidelines for Community Renewal<br>provide practical guidance for recovery practice.</p>
  <div class="flora" role="img" aria-label="Illustrated banksia cone and native leaves" style="left:258px;top:430px;width:100px;height:120px;background:radial-gradient(circle at 50% 45%,#c9652e 0 25%,#5f8a2e 48%,rgba(246,242,232,0) 72%)"></div>
</section>

<!-- Pull-up banner -->
<div class="banner-rail"></div>
<section class="sheet banner">
  <svg style="position:absolute;left:0;top:0" width="215" height="558" viewBox="0 0 215 558" aria-hidden="true">
    <path d="M0 0h215v205c-60 10-100-6-150 4S10 226 0 228z" fill="var(--navy)"/>
    <path d="M0 470c50-20 110 10 215-30v118H0z" fill="var(--teal)"/>
    <path d="M0 485c60-15 120 5 215-25v98H0z" fill="var(--navy)"/>
  </svg>
  <div class="banner-copy">
    <p class="eyebrow">SHARED GUIDELINES FOR</p>
    <h1 class="title">Community<span class="accent">Renewal</span></h1>
    <p class="tagline">Guiding recovery<br>Strengthening <em>communities</em><br>Building a <em>resilient Australia</em></p>
  </div>
  <ul class="banner-list">
    <li style="color:var(--green)"><span class="dot-icon" style="background:var(--green)"><svg><use href="#i-leaf"/></svg></span>UNDERSTANDING<br>CONTEXT</li>
    <li style="color:var(--purple)"><span class="dot-icon" style="background:var(--purple)"><svg><use href="#i-ring"/></svg></span>RECOGNISING<br>COMPLEXITY</li>
    <li style="color:var(--orange)"><span class="dot-icon" style="background:var(--orange)"><svg><use href="#i-group"/></svg></span>COMMUNITY-CENTRED<br>APPROACHES</li>
    <li style="color:var(--teal)"><span class="dot-icon" style="background:var(--teal)"><svg><use href="#i-nodes"/></svg></span>COORDINATION</li>
    <li style="color:var(--blue)"><span class="dot-icon" style="background:var(--blue)"><svg><use href="#i-chat"/></svg></span>COMMUNICATION</li>
    <li style="color:var(--yellow)"><span class="dot-icon" style="background:var(--yellow)"><svg><use href="#i-sun"/></svg></span>CAPACITY BUILDING</li>
  </ul>
  <p class="banner-foot">People. Communities. Together.<b>Stronger today,<br>resilient tomorrow.</b></p>
  <div class="flora" role="img" aria-label="Illustrated golden banksia with native foliage" style="left:145px;top:478px;width:70px;height:80px;background:radial-gradient(circle at 50% 45%,#e6b328 0 28%,#5f8a2e 50%,rgba(14,53,82,0) 75%)"></div>
</section>

<h2 class="section-label" style="left:383px;top:600px">SOCIAL MEDIA TILES <span style="font-weight:400;font-size:12px">(1080x1080px)</span></h2>

<!-- Social tiles -->
<section class="sheet tile" style="left:36px">
  <div class="tile-head"><span class="dot-icon" style="background:var(--green)"><svg><use href="#i-leaf"/></svg></span><h3 class="tile-title" style="color:var(--green)">UNDERSTANDING<br>CONTEXT</h3></div>
  <p class="tile-text">Build on local strengths, respect diversity and understand what matters to your community.</p>
  <svg class="wave" viewBox="0 0 156 40" height="40" preserveAspectRatio="none" aria-hidden="true"><path d="M0 12C40 0 90 20 156 6v34H0z" fill="var(--lime)"/><path d="M0 20C50 10 100 26 156 16v24H0z" fill="var(--green)"/></svg>
  <p class="tile-foot">People. Communities. Together.</p>
</section>
<section class="sheet tile" style="left:207px">
  <div class="tile-head"><span class="dot-icon" style="background:var(--purple)"><svg><use href="#i-ring"/></svg></span><h3 class="tile-title" style="color:var(--purple)">RECOGNISING<br>COMPLEXITY</h3></div>
  <p class="tile-text">Disasters are complex and impacts change over time. Be flexible, adapt and learn together.</p>
  <svg class="wave" viewBox="0 0 156 40" height="40" preserveAspectRatio="none" aria-hidden="true"><path d="M0 8C40 20 90 0 156 10v30H0z" fill="#9c86c4"/><path d="M0 18C50 26 100 10 156 20v20H0z" fill="var(--purple)"/></svg>
  <p class="tile-foot">People. Communities. Together.</p>
</section>
<section class="sheet tile" style="left:378px">
  <div class="tile-head"><span class="dot-icon" style="background:var(--orange)"><svg><use href="#i-group"/></svg></span><h3 class="tile-title long" style="color:var(--orange)">COMMUNITY-CENTRED<br>APPROACHES</h3></div>
  <p class="tile-text">Put communities at the centre. Empower, listen and support local leadership.</p>
  <svg class="wave" viewBox="0 0 156 40" height="40" preserveAspectRatio="none" aria-hidden="true"><path d="M0 10C40 0 100 22 156 8v32H0z" fill="#f0a35a"/><path d="M0 20C50 12 100 28 156 18v22H0z" fill="var(--orange)"/></svg>
  <p class="tile-foot">People. Communities. Together.</p>
</section>
<section class="sheet tile" style="left:549px">
  <div class="tile-head"><span class="dot-icon" style="background:var(--teal)"><svg><use href="#i-nodes"/></svg></span><h3 class="tile-title" style="color:var(--teal)">COORDINATION</h3></div>
  <p class="tile-text">Plan and work together across sectors. Share resources, align actions and adapt as needs evolve.</p>
  <svg class="wave" viewBox="0 0 156 40" height="40" preserveAspectRatio="none" aria-hidden="true"><path d="M0 6C40 18 100 0 156 12v28H0z" fill="var(--sky)"/><path d="M0 18C50 26 100 10 156 22v18H0z" fill="var(--teal)"/></svg>
  <p class="tile-foot">People. Communities. Together.</p>
</section>
<section class="sheet tile" style="left:720px">
  <div class="tile-head"><span class="dot-icon" style="background:var(--blue)"><svg><use href="#i-chat"/></svg></span><h3 class="tile-title" style="color:var(--blue)">COMMUNICATION</h3></div>
  <p class="tile-text">Communicate clearly, listen actively and share information in ways that are accessible to all.</p>
  <svg class="wave" viewBox="0 0 156 40" height="40" preserveAspectRatio="none" aria-hidden="true"><path d="M0 10C40 0 100 22 156 8v32H0z" fill="#5d8fd1"/><path d="M0 20C50 12 100 28 156 18v22H0z" fill="var(--blue)"/></svg>
  <p class="tile-foot">People. Communities. Together.</p>
</section>
<section class="sheet tile" style="left:891px">
  <div class="tile-head"><span class="dot-icon" style="background:var(--yellow)"><svg><use href="#i-sun"/></svg></span><h3 class="tile-title" style="color:var(--yellow)">CAPACITY<br>BUILDING</h3></div>
  <p class="tile-text">Strengthen skills, connections and resilience for a stronger future together.</p>
  <svg class="wave" viewBox="0 0 156 40" height="40" preserveAspectRatio="none" aria-hidden="true"><path d="M0 8C40 20 90 0 156 10v30H0z" fill="#f2c85a"/><path d="M0 18C50 26 100 10 156 20v20H0z" fill="var(--yellow)"/></svg>
  <p class="tile-foot">People. Communities. Together.</p>
</section>
</body>
</html>
```